Health and wellnes company needs business cards

We are a Health and wellness business just relocated to Spain. Here nobody knows our business so we would like to put some of our services on the card. Clean design with logo.

Contact Information for Business Card

Brightmeadow
Karin & Tobias Edvall
Calle del Olivar 17
Villaverde del Pinar
Mobile: 0046 731 402716
info@brightmeadow.example

Font styles to use
Serif

Colors
85cae6
85acd3
b768aa

Requirements
Must have
• these Services somewhere on the card
• - Private or group yoga
• - Reconnective healing
• - Kitesurfing lessons
• - Massage
• LOgo somewhere
Nice to have
• Colours that go with the logo please

```html
<!DOCTYPE html>
<html lang="en">
<head>
<meta charset="utf-8">
<title>Brightmeadow Business Card</title>
<link rel="stylesheet" href="https://fonts.googleapis.com/css2?family=Lato:wght@400;700&display=swap">
<style>
  :root {
    --navy: #1b2f5e;
    --navy-deep: #15305a;
    --navy-soft: #2a4677;
    --teal: #5cc0bf;
    --paper: #fbfbfb;
    --backdrop: #e4e5e8;
  }
  * { box-sizing: border-box; margin: 0; padding: 0; }
  html, body {
    width: 1200px; height: 1021px; overflow: hidden;
    background: var(--backdrop);
    font-family: "Lato", sans-serif;
  }
  .stage { position: relative; width: 1200px; height: 1021px; }
  .card {
    position: absolute; left: 270px; width: 660px; height: 400px;
    border-radius: 3px;
    box-shadow: 0 6px 18px rgba(0,0,0,0.18);
  }
  .card-back {
    top: 80px;
    background: var(--navy-deep);
    display: flex; align-items: center; justify-content: center; gap: 18px;
  }
  .back-mark {
    width: 26px; height: 26px; border-radius: 50%;
    border: 3px solid var(--navy-soft);
  }
  .back-name {
    font-weight: 700; font-size: 40px; letter-spacing: 2px;
    color: var(--navy-soft);
  }
  .card-front { top: 540px; background: var(--paper); color: var(--navy); }
  .brand {
    position: absolute; left: 54px; top: 66px;
    display: flex; align-items: center; gap: 12px;
  }
  .brand-dot { width: 20px; height: 20px; border-radius: 50%; background: var(--teal); }
  .brand-name { font-weight: 700; font-size: 32px; letter-spacing: 1.5px; color: var(--navy); }
  .divider {
    position: absolute; left: 48px; right: 48px; top: 176px;
    height: 2px; background: var(--teal);
  }
  .services {
    position: absolute; left: 54px; top: 196px;
    list-style: none; font-size: 18px; line-height: 24px;
  }
  .services li::before {
    content: ""; display: inline-block;
    width: 6px; height: 6px; border-radius: 50%;
    background: var(--teal); margin-right: 10px; vertical-align: middle;
  }
  .holders { position: absolute; right: 48px; top: 140px; font-weight: 700; font-size: 22px; }
  .contact {
    position: absolute; right: 48px; top: 196px;
    text-align: right; font-size: 18px; line-height: 24px;
  }
  .contact .address { margin-bottom: 14px; }
  .contact-line { display: flex; justify-content: flex-end; align-items: center; gap: 10px; }
  .contact-line svg { width: 18px; height: 18px; flex: none; }
</style>
</head>
<body>
<main class="stage">
  <section class="card card-back" aria-label="Card back">
    <span class="back-mark"></span>
    <span class="back-name">BRIGHTMEADOW</span>
  </section>

  <section class="card card-front" aria-label="Card front">
    <div class="brand">
      <span class="brand-dot"></span>
      <span class="brand-name">BRIGHTMEADOW</span>
    </div>

    <p class="holders">Karin &amp; Tobias Edvall</p>
    <div class="divider"></div>

    <ul class="services">
      <li>Private or Group Yoga</li>
      <li>Reconnective Healing</li>
      <li>Kitesurfing Lessons</li>
      <li>Massage</li>
    </ul>

    <div class="contact">
      <p class="address">Calle del Olivar 17<br>Villaverde del Pinar</p>
      <p class="contact-line">0046 731 402716
        <svg viewBox="0 0 18 18" fill="none" stroke="#5cc0bf" stroke-width="1.5"><rect x="5" y="1.5" width="8" height="15" rx="1.5"/><line x1="8" y1="14" x2="10" y2="14"/></svg>
      </p>
      <p class="contact-line">info@brightmeadow.example
        <svg viewBox="0 0 18 18" fill="none" stroke="#5cc0bf" stroke-width="1.5"><rect x="1.5" y="4" width="15" height="10" rx="1"/><polyline points="1.5,4 9,10 16.5,4"/></svg>
      </p>
      <p class="contact-line">www.brightmeadow.example
        <svg viewBox="0 0 18 18" fill="none" stroke="#5cc0bf" stroke-width="1.3"><circle cx="9" cy="9" r="7.5"/><ellipse cx="9" cy="9" rx="3.2" ry="7.5"/><line x1="1.5" y1="9" x2="16.5" y2="9"/></svg>
      </p>
    </div>
  </section>
</main>
</body>
</html>
```